I want to revise my business card design and get a more modern and up to date design.

Brolvane Handyman Sevices originated from a family-owned and operated contractor business, performing home renovation, addition, and construction work in the NYC area since 2004. Today, we specialize in reliable and affordable handyman services for residential and commercial clients In 2014, we expanded to northern New Jersey. In 2016, we brought quality home improvement and repair services to new Bucks County, PA, and nearby New Jersey areas.
Target Market(s)
Home owners and business that might be looking for a General contractor, handyman, cleaning services and Home maintenance and property.
Industry/Entity Type
Construction Company
Contact Information for Business Card
I am open to new ideas
Colors
Designer to choose colors to be used in the design.
Look and feel
Each slider illustrates characteristics of the customer's brand and the style your logo design should communicate.

```html
<!DOCTYPE html>
<html lang="en">
<head>
<meta charset="UTF-8">
<title>Brolvane Handyman Sevices – Business Card</title>
<link href="https://fonts.googleapis.com/css2?family=Roboto+Condensed:wght@400;700&family=Open+Sans:wght@400;800&display=swap" rel="stylesheet">
<style>
  :root {
    --bg: #ececec;
    --card: #ffffff;
    --red: #d9101e;
    --ink: #141414;
    --grey: #555555;
    --white: #ffffff;
  }
  * { box-sizing: border-box; margin: 0; padding: 0; }
  html, body { width: 1200px; height: 956px; overflow: hidden; background: var(--bg); }
  .canvas { position: relative; width: 1200px; height: 956px; }

  .card {
    position: absolute;
    width: 560px; height: 320px;
    background: var(--card);
    box-shadow: 0 6px 18px rgba(0,0,0,0.12);
    overflow: hidden;
  }
  .card--front { left: 40px; top: 140px; }
  .card--back { left: 600px; top: 496px; }

  /* Front */
  .brand {
    position: absolute; left: 0; right: 0; top: 62px;
    display: flex; align-items: center; justify-content: center; gap: 16px;
  }
  .brand__dot { width: 46px; height: 46px; border-radius: 50%; background: var(--red); }
  .brand__text { display: flex; flex-direction: column; }
  .brand__name {
    font-family: "Open Sans", sans-serif; font-weight: 800;
    font-size: 58px; line-height: 1; color: var(--ink); letter-spacing: -1px;
  }
  .brand__tagline {
    font-family: "Open Sans", sans-serif; font-weight: 400;
    font-size: 13px; letter-spacing: 6px; color: var(--grey); margin-top: 6px;
  }
  .services-band {
    position: absolute; left: 0; right: 0; bottom: 0; height: 112px;
    background: var(--red);
    display: flex; flex-direction: column; justify-content: center; align-items: center;
    font-family: "Roboto Condensed", sans-serif; font-weight: 700;
    color: var(--white); font-size: 19px; line-height: 1.35; text-align: center;
  }

  /* Back */
  .back-mark {
    position: absolute; left: 34px; top: 80px; width: 190px; height: 170px;
    display: flex; flex-direction: column; align-items: center; justify-content: center; gap: 10px;
  }
  .back-mark__dot { width: 70px; height: 70px; border-radius: 50%; background: var(--red); }
  .back-mark__name {
    font-family: "Open Sans", sans-serif; font-weight: 800;
    font-size: 36px; color: var(--ink); line-height: 1;
  }
  .contact-panel {
    position: absolute; left: 250px; right: 0; top: 92px; height: 140px;
    background: var(--red); color: var(--white);
    padding: 22px 22px;
    font-family: "Roboto Condensed", sans-serif;
  }
  .contact-panel__name { font-weight: 700; font-size: 25px; letter-spacing: 0.3px; margin-bottom: 12px; }
  .contact-line { display: flex; align-items: center; gap: 8px; font-size: 17px; margin-bottom: 6px; }
  .contact-line svg { width: 18px; height: 18px; flex: none; }
</style>
</head>
<body>
<main class="canvas">
  <section class="card card--front">
    <div class="brand">
      <span class="brand__dot"></span>
      <div class="brand__text">
        <span class="brand__name">Brolvane</span>
        <span class="brand__tagline">HANDYMAN SERVICES</span>
      </div>
    </div>
    <div class="services-band">
      <p>Commercial and Residential Contractor | Handyman | Technician</p>
      <p>Repair | Improve | Maintain | Remodel</p>
    </div>
  </section>

  <section class="card card--back">
    <div class="back-mark">
      <span class="back-mark__dot"></span>
      <span class="back-mark__name">Brolvane</span>
    </div>
    <div class="contact-panel">
      <p class="contact-panel__name">MARCUS DELAVEY</p>
      <p class="contact-line">
        <svg viewBox="0 0 20 20" aria-hidden="true"><circle cx="10" cy="10" r="9" fill="#fff"/><path d="M7 5.5l2 2-1 1.3c.6 1.3 1.6 2.3 2.9 2.9l1.3-1 2 2-1.2 1.6c-3.4-.5-6.1-3.2-6.6-6.6z" fill="#d9101e"/></svg>
        (215) 555-0148
      </p>
      <p class="contact-line">
        <svg viewBox="0 0 20 20" aria-hidden="true"><circle cx="10" cy="10" r="9" fill="none" stroke="#fff" stroke-width="1.6"/><rect x="5" y="6.5" width="10" height="7" fill="none" stroke="#fff" stroke-width="1.4"/><path d="M5 6.5l5 4 5-4" fill="none" stroke="#fff" stroke-width="1.4"/></svg>
        brolvanehandyman@mail.com
      </p>
    </div>
  </section>
</main>
</body>
</html>
```